Cover for Where the Quiet River Bends Beyond Our Morning

Cover for a book that describes everything that happens to a person, from pre-birth life plans through growing in compassion and wisdom to death and living in the afterlife. The information is revealed in messages from people living in the life after this life. The title is Lanterns Along the Hidden Stair of Every Soul: Gathered from Voices Dwelling in the Further Meadow. Author is T. Morven Ashdale. Book size is 6 by 9.

Target Market(s)

General

Font styles to use
Serif

```html
<!DOCTYPE html>
<html lang="en">
<head>
<meta charset="utf-8">
<title>Lanterns Along the Hidden Stair of Every Soul — Cover</title>
<link rel="stylesheet" href="https://fonts.googleapis.com/css2?family=Cinzel:wght@600;700&family=Cormorant+SC:wght@500;600&family=Cormorant+Garamond:wght@600&display=swap">
<style>
  :root {
    --page: #ffffff;
    --sky-top: #9aa8bb;
    --sky-mid: #c9d2dd;
    --haze: #eef0f1;
    --meadow: #6d6a5e;
    --meadow-dark: #23263a;
    --ink: #1b1c26;
    --violet: #6a4b98;
    --spine: #f1f1f1;
    --author-light: #f4f1ea;
  }
  * { margin: 0; padding: 0; box-sizing: border-box; }
  html, body { width: 1200px; height: 1200px; overflow: hidden; background: var(--page); }
  .canvas { position: relative; width: 1200px; height: 1200px; background: var(--page); }

  .front-cover {
    position: absolute; left: 232px; top: 194px; width: 570px; height: 880px; overflow: hidden;
  }
  .cover-photo { position: absolute; inset: 0; width: 100%; height: 100%; }

  .kicker {
    position: absolute; left: 0; right: 0; text-align: center;
    font-family: "Cinzel", serif; font-weight: 600; font-size: 21px;
    letter-spacing: 2.5px; color: var(--ink);
  }
  .kicker.line-1 { top: 64px; }
  .kicker.line-2 { top: 116px; }

  .title {
    position: absolute; left: 0; right: 0; text-align: center;
    font-family: "Cinzel", serif; font-weight: 700; font-size: 60px;
    letter-spacing: 3px; color: var(--violet); line-height: 1;
  }
  .title.line-1 { top: 162px; }
  .title.line-2 { top: 238px; }
  .title.line-3 { top: 314px; }

  .subtitle {
    position: absolute; left: 0; right: 0; top: 396px; text-align: center;
    font-family: "Cormorant SC", serif; font-weight: 600; font-size: 17px;
    letter-spacing: 1.6px; color: var(--ink);
  }

  .author {
    position: absolute; left: 0; right: 0; top: 785px; text-align: center;
    font-family: "Cormorant Garamond", serif; font-weight: 600; font-size: 25px;
    letter-spacing: 1.5px; color: var(--author-light);
  }

  .spine {
    position: absolute; left: 838px; top: 194px; width: 106px; height: 880px; background: var(--spine);
  }
  .spine-author {
    position: absolute; left: 76px; top: 94px; writing-mode: vertical-rl;
    font-family: "Cormorant Garamond", serif; font-weight: 600; font-size: 19px;
    letter-spacing: 1px; color: var(--ink);
  }
  .spine-title {
    position: absolute; top: 428px; right: 12px; height: 420px;
    writing-mode: vertical-rl; display: flex; flex-direction: column; align-items: flex-start;
  }
  .spine-kicker {
    font-family: "Cinzel", serif; font-weight: 600; font-size: 13px;
    letter-spacing: 1.2px; color: var(--ink); line-height: 22px;
  }
  .spine-main {
    font-family: "Cinzel", serif; font-weight: 700; font-size: 24px;
    letter-spacing: 1.5px; color: var(--violet); line-height: 30px;
  }
  .spine-sub {
    font-family: "Cormorant SC", serif; font-weight: 600; font-size: 11.5px;
    letter-spacing: 0.8px; color: var(--ink); line-height: 20px;
  }
</style>
</head>
<body>
<main class="canvas">
  <section class="front-cover">
    <svg class="cover-photo" viewBox="0 0 570 880" preserveAspectRatio="none" role="img"
         aria-label="Photograph: overcast sky above a sunlit meadow of tall grasses and wildflowers among old headstones, with an open hand reaching upward">
      <defs>
        <linearGradient id="sceneTone" x1="0" y1="0" x2="0" y2="1">
          <stop offset="0" stop-color="var(--sky-top)"/>
          <stop offset="0.35" stop-color="var(--sky-mid)"/>
          <stop offset="0.6" stop-color="var(--haze)"/>
          <stop offset="0.72" stop-color="var(--meadow)"/>
          <stop offset="1" stop-color="var(--meadow-dark)"/>
        </linearGradient>
      </defs>
      <rect width="570" height="880" fill="url(#sceneTone)"/>
    </svg>

    <p class="kicker line-1">LANTERNS ALONG</p>
    <p class="kicker line-2">THE HIDDEN</p>
    <h1 class="title line-1">STAIR</h1>
    <h1 class="title line-2">OF EVERY</h1>
    <h1 class="title line-3">SOUL</h1>
    <p class="subtitle">Gathered from Voices Dwelling in the Further Meadow</p>
    <p class="author">T. Morven Ashdale, PhD</p>
  </section>

  <aside class="spine">
    <p class="spine-author">T. Morven Ashdale, PhD</p>
    <div class="spine-title">
      <span class="spine-kicker">LANTERNS ALONG THE HIDDEN</span>
      <span class="spine-main">STAIR OF EVERY SOUL</span>
      <span class="spine-sub">Gathered from Voices Dwelling in the Further Meadow</span>
    </div>
  </aside>
</main>
</body>
</html>
```